Mineral Drinking Water Label Design

We need a label design for a new bottled drinking water based in (either Pwani or Dar Es Salaam, decision is not yet finalized), Tanzania on the coast of East Africa.

We will use underground aquifers as our only source of raw water(pre treated water).

Which will then be treated through osmosis process, then the mineral water will be bottled in standard 500ml, 1000ml and 1500 ml plastic PET bottles for customer consumption.

We have a vision of expanding our supply network to cover the entire country. Therefore, we expect the label to communicate trust, purity, cleanliness, healthiness of water contained.

The uniqueness and attractiveness of the label/logo is of utmost importance.

With regards to water brand name, we prefer that you use your own imagination and creativity to come up with a name that might be more suited to your individual design.

Note: Different shades of blue are mainly associated with drinking water in Tanzania, however feel free to use any other colors.

Target Market(s)

Upper Class citizens, Hotels, Large Supermarkets etc

Font styles to use
Script

Colors

Designer to choose colors to be used in the design.

```html
<!DOCTYPE html>
<html lang="en">
<head>
<meta charset="utf-8">
<title>Zevai Water Label Variations</title>
<link rel="stylesheet" href="https://fonts.googleapis.com/css2?family=Great+Vibes&family=Josefin+Sans:wght@700&family=Montserrat:wght@400;500&family=Open+Sans:wght@400&display=swap">
<style>
  :root {
    --page: #ffffff;
    --ink: #111111;
    --water: #0ba1d1;
    --peak-light: #cbe9f4;
    --peak-mid: #8fd1ea;
    --peak-deep: #2fa9d8;
    --line-grey: #f3f5f6;
    --text-on-blue: #ffffff;
  }
  * { margin: 0; padding: 0; box-sizing: border-box; }
  html, body { width: 1200px; height: 1025px; overflow: hidden; background: var(--page); }
  .canvas { position: relative; width: 1200px; height: 1025px; }

  .label { position: absolute; }
  .label > svg.label-shape { position: absolute; inset: 0; width: 100%; height: 100%; }
  .label .line { position: absolute; left: 0; width: 100%; text-align: center; white-space: nowrap; }

  .label--outline { left: 159px; top: 98px; width: 334px; height: 333px; color: var(--ink); }
  .label--shield { left: 730px; top: 98px; width: 334px; height: 333px; color: var(--text-on-blue); }
  .label--wide { left: 160px; top: 651px; width: 341px; height: 222px; color: var(--text-on-blue); }
  .label--square { left: 744px; top: 599px; width: 310px; height: 287px; color: var(--text-on-blue); }

  .script { font-family: "Great Vibes", cursive; font-size: 24px; line-height: 1; }
  .brand { font-family: "Josefin Sans", sans-serif; font-weight: 700; line-height: 1; letter-spacing: 1px; }
  .tagline { font-family: "Montserrat", sans-serif; font-weight: 500; font-size: 11px; letter-spacing: 0.6px; line-height: 1; }
  .body-copy { font-family: "Montserrat", sans-serif; font-size: 10.5px; letter-spacing: 0.5px; line-height: 13.5px; }
  .volume { font-family: "Open Sans", sans-serif; font-size: 18px; line-height: 1; }

  .mark { position: absolute; width: 15px; height: 15px; border-radius: 50%; font-family: "Montserrat", sans-serif; font-weight: 500; font-size: 9px; line-height: 15px; text-align: center; }
  .label--outline .mark { border: 1.2px solid var(--ink); line-height: 13px; }
  .label--shield .mark, .label--wide .mark, .label--square .mark { background: var(--text-on-blue); color: var(--water); }
</style>
</head>
<body>
<main class="canvas">

  <section class="label label--outline">
    <svg class="label-shape" viewBox="0 0 334 333">
      <path d="M0.5,35 H333.5 V150 A166.5,182.5 0 0 1 0.5,150 Z" fill="#ffffff" stroke="#222" stroke-width="1"/>
      <rect x="0.5" y="0.5" width="333" height="92" fill="var(--line-grey)" stroke="#222" stroke-width="1" role="img" aria-label="Line drawing of layered mountain ridges above water"/>
    </svg>
    <p class="line script" style="top:112px; left:-18px;">Original</p>
    <p class="line brand" style="top:147px; font-size:74px;">ZEVAI</p>
    <span class="mark" style="left:312px; top:128px;">R</span>
    <p class="line tagline" style="top:213px;">LOREM IPSUM LOREM IPSUM LOREM</p>
    <p class="line body-copy" style="top:237px;">LOREM IPSUM LOREM IPSUM LOREM IPSUM<br>LOREM IPSUM LOREM IPSUM<br>LOREM IPSUM</p>
    <p class="line volume" style="top:295px;">1000 ml</p>
  </section>

  <section class="label label--shield">
    <svg class="label-shape" viewBox="0 0 334 333">
      <defs>
        <linearGradient id="ridge-shield" x1="0" y1="0" x2="0" y2="1">
          <stop offset="0" stop-color="var(--peak-light)"/>
          <stop offset="0.55" stop-color="var(--peak-mid)"/>
          <stop offset="1" stop-color="var(--peak-deep)"/>
        </linearGradient>
      </defs>
      <path d="M0,35 H334 V150 A167,183 0 0 1 0,150 Z" fill="var(--water)"/>
      <rect x="0" y="0" width="334" height="93" fill="url(#ridge-shield)" role="img" aria-label="Layered blue mountain ridges above a lake"/>
    </svg>
    <p class="line script" style="top:112px; left:-18px;">Original</p>
    <p class="line brand" style="top:147px; font-size:74px;">ZEVAI</p>
    <span class="mark" style="left:288px; top:133px;">R</span>
    <p class="line tagline" style="top:213px;">LOREM IPSUM LOREM IPSUM LOREM</p>
    <p class="line body-copy" style="top:237px;">LOREM IPSUM LOREM IPSUM LOREM IPSUM<br>LOREM IPSUM LOREM IPSUM<br>LOREM IPSUM</p>
    <p class="line volume" style="top:295px;">1000 ml</p>
  </section>

  <section class="label label--wide">
    <svg class="label-shape" viewBox="0 0 341 222">
      <defs>
        <linearGradient id="ridge-wide" x1="0" y1="0" x2="0" y2="1">
          <stop offset="0" stop-color="var(--peak-light)"/>
          <stop offset="0.55" stop-color="var(--peak-mid)"/>
          <stop offset="1" stop-color="var(--peak-deep)"/>
        </linearGradient>
      </defs>
      <path d="M0,30 H341 V198 A24,24 0 0 1 317,222 H24 A24,24 0 0 1 0,198 Z" fill="var(--water)"/>
      <rect x="0" y="0" width="341" height="101" fill="url(#ridge-wide)" role="img" aria-label="Layered blue mountain ridges above a lake"/>
    </svg>
    <p class="line brand" style="top:114px; font-size:92px;">ZEVAI</p>
    <span class="mark" style="left:318px; top:98px;">R</span>
    <p class="line tagline" style="top:193px; font-size:12.5px;">LOREM IPSUM LOREM IPSUM LOREM</p>
  </section>

  <section class="label label--square">
    <svg class="label-shape" viewBox="0 0 310 287">
      <defs>
        <linearGradient id="ridge-square" x1="0" y1="0" x2="0" y2="1">
          <stop offset="0" stop-color="var(--peak-light)"/>
          <stop offset="0.55" stop-color="var(--peak-mid)"/>
          <stop offset="1" stop-color="var(--peak-deep)"/>
        </linearGradient>
      </defs>
      <rect x="0" y="30" width="310" height="257" fill="var(--water)"/>
      <rect x="0" y="0" width="310" height="88" fill="url(#ridge-square)" role="img" aria-label="Layered blue mountain ridges above a lake"/>
    </svg>
    <p class="line script" style="top:104px; left:-18px;">Original</p>
    <p class="line brand" style="top:136px; font-size:64px;">ZEVAI</p>
    <span class="mark" style="left:268px; top:126px;">R</span>
    <p class="line tagline" style="top:195px;">LOREM IPSUM LOREM IPSUM LOREM</p>
    <p class="line body-copy" style="top:218px;">LOREM IPSUM LOREM IPSUM LOREM IPSUM<br>LOREM IPSUM LOREM IPSUM<br>LOREM IPSUM</p>
    <p class="line volume" style="top:258px; left:auto; right:12px; width:auto;">1000 ml</p>
  </section>

</main>
</body>
</html>
```